Cybersecurity company is looking for business card.

I need a business card design for our company, we are a cybersecurity company providing advance technology to protect agains any kind of malware. We need a fresh modern design it should communicate modern, technology and growth.

Target Market(s)

Business to business

Industry/Entity Type

Business

Contact Information for Business Card

Should have location, address, fax, mobile, phone, email and website.

Requirements
Must have
• Must follow company's logo color and style. Must have the company's log on its.

```html
<!DOCTYPE html>
<html lang="en">
<head>
<meta charset="utf-8">
<title>vortiq business card</title>
<link rel="stylesheet" href="https://fonts.googleapis.com/css2?family=Lato:wght@400;700;900&display=swap">
<style>
  :root {
    --red: #a3161b;
    --black: #0b0b0b;
    --white: #ffffff;
    --ink: #111111;
    --backdrop: #e4e4e4;
  }
  * { box-sizing: border-box; margin: 0; padding: 0; }
  html, body {
    width: 1200px; height: 926px; overflow: hidden;
    background: var(--backdrop);
    font-family: "Lato", sans-serif;
  }
  .sheet {
    position: relative; width: 1200px; height: 926px;
    display: flex; flex-direction: column; align-items: center;
    justify-content: center; gap: 42px;
  }
  .card {
    position: relative; width: 700px; height: 400px; overflow: hidden;
    box-shadow: 0 6px 18px rgba(0,0,0,0.18);
  }
  .card-corner { position: absolute; top: 0; left: 0; width: 96px; height: 42px; }

  /* front */
  .card-front { background: var(--white); }
  .brand-name {
    font-family: "Lato", sans-serif; font-weight: 900; letter-spacing: 1px;
    line-height: 1;
  }
  .card-front .brand-name {
    position: absolute; left: 56px; top: 128px; font-size: 50px; color: var(--ink);
  }
  .holder {
    position: absolute; left: 368px; top: 104px; font-size: 30px; color: var(--ink);
    font-weight: 400;
  }
  .holder strong { font-weight: 700; }
  .title-band {
    position: absolute; left: 358px; top: 146px; right: 0; height: 24px;
    background: var(--red); color: var(--white);
    font-size: 13px; font-weight: 700; padding: 4px 0 0 10px;
  }
  .contact-list {
    position: absolute; left: 360px; top: 186px; list-style: none;
  }
  .contact-item {
    display: flex; align-items: center; height: 25px; font-size: 17px; color: var(--ink);
  }
  .contact-label {
    background: var(--red); color: var(--white); font-weight: 700;
    font-size: 14px; padding: 1px 6px 2px; margin-right: 7px; line-height: 1.2;
  }
  .address-band {
    position: absolute; left: 0; right: 0; bottom: 0; height: 46px;
    background: var(--black); color: var(--white);
    font-size: 15px; font-weight: 700; letter-spacing: 1.6px;
    display: flex; align-items: center; padding-left: 28px;
  }

  /* back */
  .card-back { background: var(--black); }
  .card-back .brand-name {
    position: absolute; left: 0; right: 0; top: 150px; text-align: center;
    font-size: 96px; color: var(--white);
  }
</style>
</head>
<body>
<main class="sheet">
  <section class="card card-front" aria-label="Business card front">
    <svg class="card-corner" viewBox="0 0 96 42" aria-hidden="true"><polygon points="0,0 96,0 0,42" fill="var(--red)"/></svg>
    <div class="brand-name">vortiq</div>
    <h1 class="holder">Daniel <strong>Harper</strong></h1>
    <div class="title-band">title goes here</div>
    <ul class="contact-list">
      <li class="contact-item"><span class="contact-label">cell:</span>+971 55 480 XXXX</li>
      <li class="contact-item"><span class="contact-label">phone:</span>04 560 XXXX</li>
      <li class="contact-item"><span class="contact-label">fax:</span>04 560 XXXX</li>
      <li class="contact-item"><span class="contact-label">email:</span>name.surname@vortiq.com</li>
      <li class="contact-item"><span class="contact-label">website:</span>www.vortiq.com</li>
    </ul>
    <div class="address-band">Harbor Tech Park (HTP) -Meridian Avenue. Coastline - UAE</div>
  </section>

  <section class="card card-back" aria-label="Business card back">
    <svg class="card-corner" viewBox="0 0 96 42" aria-hidden="true"><polygon points="0,0 96,0 0,42" fill="var(--red)"/></svg>
    <div class="brand-name">vortiq</div>
  </section>
</main>
</body>
</html>
```